Pale Lanterns Old Lane Walk Poster Design

We need an A4 sized poster to promote our weekly true crime tours. This poster will be posted onto community noticeboards.
Lots of information and images can be viewed at the following links:-
www.palelanterns.com.au
www.palelanterns.com.au/bookings/
https://www.facebook.com/palelanternsoldlane/
https://www.examplereviews.com.au/Attraction_Review-g000000-d00000000-Reviews-Pale_Lanterns-Newcastle_Greater_Newcastle_New_South_Wales.html
There are also a number of images for possible use at the following link - we are open to intepretation:-
http://palelanterns.com.au/tour-photographs/
The font on our website is "SpecialElite" so we would like to continue using that font type.
Target Market(s)
Adults 25-65.
Font styles to use
Other font styles liked:
- Special Elite
Colors
Designer to choose colors to be used in the design.
Look and feel
Each slider illustrates characteristics of the customer's brand and the style your logo design should communicate.

```html
<!DOCTYPE html>
<html lang="en">
<head>
<meta charset="utf-8">
<title>Pale Lanterns Old Lane Walk</title>
<link rel="stylesheet" href="https://fonts.googleapis.com/css2?family=Special+Elite&family=Courier+Prime&family=Poppins:wght@400;500&display=block">
<style>
  :root {
    --red: #e1262d;
    --white: #ffffff;
    --ink: #1c1c1c;
    --text: #f2f2f2;
    --type: "Special Elite", "Courier Prime", "Courier New", monospace;
  }
  * { margin: 0; padding: 0; box-sizing: border-box; }
  html, body { width: 849px; height: 1200px; overflow: hidden; background: var(--ink); }
  .poster {
    position: relative;
    width: 849px; height: 1200px; overflow: hidden;
    background: linear-gradient(180deg, #4a4a4a 0%, #2e2e2e 55%, #1f1f1f 80%, #161616 100%);
    font-family: "Poppins", sans-serif;
    color: var(--text);
  }
  .hero-photo {
    position: absolute; left: 0; top: 0; width: 849px; height: 680px;
    background:
      radial-gradient(ellipse at 45% 55%, rgba(170,170,170,.55) 0%, rgba(120,120,120,.25) 40%, rgba(0,0,0,0) 70%),
      linear-gradient(180deg, #5c5c5c 0%, #7c7c7c 40%, #6a6a6a 62%, #3a3a3a 85%, rgba(46,46,46,0) 100%);
  }
  .title {
    position: absolute; left: 0; top: 32px; width: 849px;
    text-align: center; font-weight: normal;
  }
  .title-line {
    display: inline-block;
    background: var(--red); color: var(--white);
    font-family: var(--type); font-weight: normal;
    font-size: 60px; line-height: 68px;
    padding: 0 14px; margin-bottom: 8px;
  }
  .tagline {
    position: absolute; left: 20px; top: 612px;
    font-family: var(--type); font-weight: normal;
    font-size: 31px; line-height: 36px; letter-spacing: 1px;
    color: var(--white); text-transform: uppercase;
  }
  .highlights { position: absolute; left: 20px; top: 707px; list-style: none; }
  .highlights li {
    position: relative; padding-left: 15px;
    font-size: 16px; line-height: 20px; margin-bottom: 21.5px;
  }
  .highlights li::before {
    content: ""; position: absolute; left: 0; top: 7px;
    width: 6px; height: 6px; background: var(--red);
  }
  .claim-band {
    position: absolute; left: 165px; top: 915px; width: 684px; height: 72px;
    background: var(--red); color: var(--white);
    font-family: var(--type); font-size: 34px;
    display: flex; align-items: center; padding-left: 24px;
  }
  .meeting-point {
    position: absolute; right: 24px; top: 996px; width: 780px;
    text-align: right; font-size: 16px; line-height: 33px;
  }
  .price-block { position: absolute; left: 17px; top: 1076px; }
  .price { font-family: var(--type); font-size: 34px; line-height: 40px; color: var(--white); }
  .price-block p { font-size: 15.5px; line-height: 38px; }
  .divider { position: absolute; top: 1088px; width: 3px; height: 104px; background: var(--red); }
  .divider.left { left: 312px; }
  .divider.right { left: 580px; }
  .booking-note {
    position: absolute; left: 315px; width: 265px; top: 1102px;
    text-align: center; font-family: var(--type);
    font-size: 32px; line-height: 38px; color: var(--white); letter-spacing: 1px;
  }
  .brand-mark {
    position: absolute; left: 583px; width: 266px; top: 1122px;
    display: flex; align-items: center; justify-content: center; gap: 10px;
    font-family: "Poppins", sans-serif; font-weight: 500; font-size: 22px;
    color: var(--white); letter-spacing: 1px; text-transform: uppercase;
  }
  .brand-mark .square { width: 14px; height: 14px; background: var(--white); }
</style>
</head>
<body>
<main class="poster">
  <div class="hero-photo" role="img" aria-label="Black and white photograph of a rainy old city street at dusk with a tram and a lone pedestrian"></div>

  <h1 class="title">
    <span class="title-line">Pale Lanterns</span><br>
    <span class="title-line">Old Lane Walk</span>
  </h1>

  <h2 class="tagline">Take a walk on the dark side -<br>revisit the scenes of the crimes.</h2>

  <ul class="highlights">
    <li>Retrace the steps of Port Halden's most infamous murderers.</li>
    <li>Descend into the murky world of fraudsters, adulterers and lordly impersonators.</li>
    <li>Unearth the keys to the heart of the Lamplight Murderer.</li>
    <li>Relive a time that proves truth is far stranger than fiction.</li>
    <li>Book your ticket for a unique investigation into a dark and crime ridden history.</li>
  </ul>

  <div class="claim-band">100% TRUE - 100% UNBELIEVABLE</div>

  <p class="meeting-point">Meets at the corner of Harbour Row &amp; Lantern Lane, Port Halden; adjacent to the Old Bond Store<br>and the Quarry Yard.&nbsp; Bring comfortable shoes.</p>

  <div class="price-block">
    <div class="price">$34.00</div>
    <p>Duration: 90 Minutes (approx.)</p>
    <p>Location: Halden East, NSW</p>
  </div>

  <span class="divider left"></span>
  <div class="booking-note">BOOKINGS<br>ESSENTIAL.</div>
  <span class="divider right"></span>

  <div class="brand-mark"><span class="square"></span>Pale Lanterns</div>
</main>
</body>
</html>
```